Business Card Design For A Renovation Contractor Company

We need a business card for a new company based in Singapore, our company name is "KT Planora". We are a renovation contractor that builds designs into reality. We build more of F&B restaurants, retail stores and commercial offices. We work very closely with designers. The final design should communicate to our client that we are a company that you can trust, that will plan and complete your project without giving you a headache. I like my client to remember my company as "KT". The beauty of SIMPLE is important.

Industry/Entity Type

Contractor

Requirements
Nice to have
• Black or Red base

```html
<!DOCTYPE html>
<html lang="en">
<head>
<meta charset="utf-8">
<title>KT Planora – Business Card</title>
<link href="https://fonts.googleapis.com/css2?family=Arimo:wght@400;700&display=swap" rel="stylesheet">
<style>
  :root {
    --backdrop: #4a4a4c;
    --card-frame: #262626;
    --brand-red: #ef4f4f;
    --tab-red: #e8323a;
    --tab-fold: #c9222b;
    --paper: #f4f4f2;
    --ink: #333333;
    --white: #ffffff;
  }
  html, body {
    margin: 0;
    padding: 0;
    width: 1200px;
    height: 1059px;
    overflow: hidden;
    background: var(--backdrop);
    font-family: "Arimo", Arial, sans-serif;
  }
  .stage { position: relative; width: 1200px; height: 1059px; }
  .card {
    position: absolute;
    left: 267px;
    width: 665px;
    height: 381px;
  }
  .card--front { top: 111px; }
  .card--back { top: 566px; }
  .card__shape { position: absolute; inset: 0; }
  .card__text { position: absolute; margin: 0; white-space: nowrap; }

  /* front */
  .front-ring {
    position: absolute; left: 284px; top: 107px;
    width: 94px; height: 94px; border: 5px solid var(--white);
    border-radius: 50%; box-sizing: border-box;
  }
  .front-name {
    left: 0; width: 665px; top: 205px; text-align: center;
    color: var(--white); font-size: 46px; font-weight: 400; letter-spacing: 0.5px;
  }
  .front-tagline {
    left: 0; width: 665px; top: 259px; text-align: center;
    color: var(--white); font-size: 16px; letter-spacing: 0.4px;
  }

  /* back */
  .back-address { left: 80px; top: 62px; color: var(--ink); font-size: 16px; }
  .back-person { left: 112px; top: 152px; color: var(--ink); font-size: 21px; font-weight: 700; }
  .back-role { left: 112px; top: 178px; color: var(--ink); font-size: 16px; }
  .back-email { left: 135px; top: 204px; color: var(--ink); font-size: 16px; }
  .back-web { left: 80px; top: 306px; color: var(--ink); font-size: 16px; }
  .back-ring {
    position: absolute; left: 437px; top: 144px;
    width: 50px; height: 50px; border: 4px solid var(--tab-red);
    border-radius: 50%; box-sizing: border-box;
  }
  .back-brand { left: 389px; width: 150px; top: 198px; text-align: center; color: var(--ink); font-size: 25px; }
  .back-tagline { left: 389px; width: 150px; top: 229px; text-align: center; color: var(--ink); font-size: 9.5px; }
  .icon { position: absolute; }
</style>
</head>
<body>
<main class="stage">

  <!-- Front of card -->
  <section class="card card--front" aria-label="Card front">
    <svg class="card__shape" width="665" height="381" viewBox="0 0 665 381">
      <rect width="665" height="381" fill="var(--card-frame)"/>
      <path transform="translate(25 29)" fill="var(--brand-red)"
        d="M25 0 H591 A25 25 0 0 1 616 25 V70 Q616 80 604 80 H596 Q586 80 586 90 V230 Q586 240 596 240 H604 Q616 240 616 250 V299 A25 25 0 0 1 591 324 H25 A25 25 0 0 1 0 299 V250 Q0 240 12 240 H20 Q30 240 30 230 V90 Q30 80 20 80 H12 Q0 80 0 70 V25 A25 25 0 0 1 25 0 Z"/>
      <polygon points="25,232 62,232 25,264" fill="var(--tab-fold)"/>
      <rect x="23" y="151" width="79" height="81" rx="8" fill="var(--tab-red)"/>
      <polygon points="641,232 604,232 641,264" fill="var(--tab-fold)"/>
      <rect x="563" y="151" width="79" height="81" rx="8" fill="var(--tab-red)"/>
    </svg>
    <div class="front-ring"></div>
    <p class="card__text front-name">KT Planora</p>
    <p class="card__text front-tagline">planning spaces, built right</p>
  </section>

  <!-- Back of card -->
  <section class="card card--back" aria-label="Card back">
    <svg class="card__shape" width="665" height="381" viewBox="0 0 665 381">
      <rect width="665" height="381" fill="var(--card-frame)"/>
      <path transform="translate(25 30)" fill="var(--paper)"
        d="M25 0 H591 A25 25 0 0 1 616 25 V69 Q616 79 604 79 H596 Q586 79 586 89 V232 Q586 242 596 242 H604 Q616 242 616 252 V296 A25 25 0 0 1 591 321 H25 A25 25 0 0 1 0 296 V252 Q0 242 12 242 H20 Q30 242 30 232 V89 Q30 79 20 79 H12 Q0 79 0 69 V25 A25 25 0 0 1 25 0 Z"/>
      <polygon points="25,227 62,227 25,259" fill="var(--tab-fold)"/>
      <rect x="23" y="148" width="79" height="79" rx="8" fill="var(--tab-red)"/>
      <polygon points="641,227 604,227 641,259" fill="var(--tab-fold)"/>
      <rect x="563" y="148" width="79" height="79" rx="8" fill="var(--tab-red)"/>
    </svg>

    <svg class="icon" style="left:57px;top:64px" width="16" height="15" viewBox="0 0 16 15" aria-hidden="true">
      <path d="M8 0 L16 7 H13.5 V15 H10 V10 H6 V15 H2.5 V7 H0 Z" fill="var(--ink)"/>
    </svg>
    <p class="card__text back-address">Seralin Road, #07-2204 Seralin Complex, Singapore 437812</p>

    <p class="card__text back-person">Marcus Tan</p>
    <p class="card__text back-role">Position Director</p>
    <svg class="icon" style="left:112px;top:207px" width="16" height="13" viewBox="0 0 16 13" aria-hidden="true">
      <path d="M0 4 L8 0 L16 4 V13 H0 Z" fill="var(--ink)"/>
      <path d="M2 5 L8 9 L14 5" stroke="var(--paper)" stroke-width="1.4" fill="none"/>
    </svg>
    <p class="card__text back-email">marcus@ktplanora.com</p>

    <div class="back-ring"></div>
    <p class="card__text back-brand">KT Planora</p>
    <p class="card__text back-tagline">planning spaces, built right</p>

    <svg class="icon" style="left:57px;top:308px" width="16" height="16" viewBox="0 0 16 16" aria-hidden="true">
      <circle cx="8" cy="8" r="7.5" fill="var(--ink)"/>
      <path d="M0.5 8 H15.5 M8 0.5 V15.5 M2 4.5 H14 M2 11.5 H14" stroke="var(--paper)" stroke-width="0.9"/>
      <ellipse cx="8" cy="8" rx="3.3" ry="7.5" fill="none" stroke="var(--paper)" stroke-width="0.9"/>
    </svg>
    <p class="card__text back-web">www.ktplanora.com</p>
  </section>

</main>
</body>
</html>
```